Tech business card design

We need an amazing business card design for our new business 'Brakka' a marketing tech startup based in Sydney, Australia. We provide an online marketplace for businesses to search and buy advertising media, connect with service providers and learn more about marketing. We wish to communicate 'cool tech', reliability and professionalism and design based around our logo.

Target Market(s)

Business Owners

Contact Information for Business Card

Name
Position
Email Address
Website
Phone Number

Font styles to use
Other font styles liked:
• Avenir & Avenir Next

Colors

Designer to choose colors to be used in the design.

```html
<!DOCTYPE html>
<html lang="en">
<head>
<meta charset="utf-8">
<title>Brakka – Business Card</title>
<link href="https://fonts.googleapis.com/css2?family=Nunito+Sans:wght@400;600;800&display=swap" rel="stylesheet">
<style>
  :root {
    --navy: #12103a;
    --navy-soft: #232058;
    --ink: #3a3a44;
    --paper: #ffffff;
    --mist: #e4e4ee;
    --board-light: #e6e7e9;
    --board-dark: #cfd0d2;
    --light: #ffffff;
  }
  * { margin: 0; padding: 0; box-sizing: border-box; }
  html, body { width: 800px; height: 1200px; overflow: hidden; }
  body {
    font-family: "Nunito Sans", "Avenir Next", Avenir, sans-serif;
    background: radial-gradient(ellipse at 50% 48%, var(--board-light) 0%, var(--board-dark) 75%);
    position: relative;
  }
  .card {
    position: absolute;
    left: 177px;
    width: 504px;
    height: 288px;
    overflow: hidden;
  }
  .card--front { top: 156px; background: var(--paper); }
  .card--back {
    top: 693px;
    background: var(--navy);
    display: flex;
    align-items: center;
    justify-content: center;
  }
  .card__accent {
    position: absolute;
    left: 226px;
    top: 14px;
    width: 60px;
    height: 260px;
    background: linear-gradient(180deg, rgba(228,228,238,0) 0%, var(--mist) 30%, var(--mist) 70%, rgba(228,228,238,0) 100%);
  }
  .card__field {
    position: absolute;
    inset: 0;
    background:
      radial-gradient(ellipse at 12% 80%, var(--navy-soft) 0%, rgba(35,32,88,0) 45%),
      radial-gradient(ellipse at 88% 25%, var(--navy-soft) 0%, rgba(35,32,88,0) 45%),
      var(--navy);
  }
  .wordmark {
    font-weight: 800;
    letter-spacing: -1px;
    line-height: 1;
    font-size: 52px;
  }
  .card--front .wordmark {
    position: absolute;
    left: 30px;
    top: 108px;
    color: var(--navy);
  }
  .card--back .wordmark {
    position: relative;
    color: var(--light);
    margin-top: -12px;
  }
  .identity {
    position: absolute;
    left: 312px;
    top: 76px;
    color: var(--navy);
  }
  .identity__name { font-size: 25px; font-weight: 600; line-height: 1; }
  .identity__role { font-size: 14.5px; font-weight: 400; color: var(--ink); line-height: 1; margin-top: 2px; }
  .contacts {
    position: absolute;
    left: 312px;
    top: 138px;
    list-style: none;
    color: var(--ink);
    font-size: 14px;
  }
  .contacts li { display: flex; align-items: center; height: 25px; }
  .contacts svg { width: 9px; height: 9px; margin-right: 7px; fill: var(--navy); }
</style>
</head>
<body>

<section class="card card--front" aria-label="Business card front">
  <div class="card__accent" role="img" aria-label="Decorative tech line motif"></div>

  <div class="wordmark">brakka</div>

  <div class="identity">
    <div class="identity__name">Mara Quinlan</div>
    <div class="identity__role">Managing Director</div>
  </div>

  <ul class="contacts">
    <li><svg viewBox="0 0 10 10"><path d="M2,0.5 L4,2.5 L3,3.6 Q4,6 6.4,7 L7.5,6 L9.5,8 L8,9.5 Q2,9 0.5,2 Z"/></svg>0142-618-305</li>
    <li><svg viewBox="0 0 10 10"><path d="M0.5,2 H9.5 V8 H0.5 Z"/></svg>info@brakkamedia.com</li>
    <li><svg viewBox="0 0 10 10"><circle cx="5" cy="5" r="4.5"/></svg>www.brakkamedia.com</li>
  </ul>
</section>

<section class="card card--back" aria-label="Business card back">
  <div class="card__field" role="img" aria-label="Decorative tech pattern in navy tones"></div>
  <div class="wordmark">brakka</div>
</section>

</body>
</html>
```